Travel Itinary for Premium segment

Hi all the best designers on Pixelbazaar,
We are a travel agency specialized on the premium segment that travels to New Zealand (www.ferntidejourneys.example – please check out the video on our home page to get a good idea of our brand in a few min). We have an exciting project available.
We want to create a branded itinerary template - based on a previous version that we have (please see links below) + market inspiration (from competitors, other luxury brands), and your creativity. Clients need to be able to view it on mobile as well. The template should represent luxury, elegance, wanderlust. This is the first document the customer will receive from us once the trip details are confirmed.
It should include:
- Front page
- Thank you page (thank you for choosing Fern Tide, with our founder’s photo, signature + a short message that I will send you once we confirm),
- Itinerary overview visual (beautiful pictures and short descriptions with focus on the locations summarizing the whole trip – see links below for inspiration)
- A more detailed itinerary overview (giving the client an overview of the activities per day - see competitor example below)
- Details about each day
- Contact info (this could be included on the thank you page or on the backside
Resources:
- Inspiration from competitor: https://files.sharebox.example/s/k4mq8z/Wandora%20Sample%20Itinerary%20-%2021%20DAYS.pdf
- This is the itinerary that should be laid out in the template:
https://docs.writepad.example/document/d/7hQpL2vXn9RtY4eWc8sKz3mB6fJa1uDg5oNi0CyTrE/edit
- this is the branded look and style; https://files.sharebox.example/s/r7tn2w/0753%20FTJ%20Presentation%2016by9%201.4-Brazil.indd
- Here are the Indesign files https://files.sharebox.example/sh/p2vc9d/BBBxkRtm4
- This is what the textured brand background should look like https://files.sharebox.example/s/h8yj3f/0753%20FTJ%20Itinerary%20Overview%201.7.pdf
- Fern Tide Fonts https://files.sharebox.example/s/z5nb6c/Arno%20Pro%20Bold%20Italic%20SmText.zip
https://files.sharebox.example/s/d3wq1x/Arno%20Pro%20Semibold%20Italic%20Display.zip
Are you up for this? Please confirm asap if you will be able to do it, by providing concepts. If we like the concepts we can go ahead.
Look forward to hearing from you.
Thanks,

```html
<!DOCTYPE html>
<html lang="en">
<head>
<meta charset="utf-8">
<title>Fern Tide – Itinerary Cover</title>
<link rel="stylesheet" href="https://fonts.googleapis.com/css2?family=Questrial&family=Cormorant+Garamond:wght@500&display=swap">
<style>
  :root {
    --bg: #e4e5e7;
    --charcoal: #3b3b3c;
    --charcoal-deep: #2e2e2f;
    --gold: #8b7a4c;
    --gold-text: #a88f4e;
    --white: #ffffff;
    --sky: #5a8fe0;
    --sea: #1f5f95;
    --lagoon: #2aa39a;
    --hill: #4f7f2c;
  }
  * { margin: 0; padding: 0; box-sizing: border-box; }
  html, body { width: 950px; height: 1200px; overflow: hidden; }
  body {
    background: var(--bg);
    font-family: "Questrial", "Century Gothic", sans-serif;
    position: relative;
  }
  .spread {
    position: absolute;
    left: 15px; top: 300px;
    width: 920px; height: 600px;
    display: flex;
    box-shadow: 0 14px 30px rgba(0,0,0,.22);
  }
  .page { position: relative; width: 460px; height: 600px; overflow: hidden; background: var(--charcoal); }

  .photo {
    position: absolute; top: 0; height: 100%;
    background: linear-gradient(180deg, var(--sky) 0%, #8fb6ea 20%, var(--sea) 26%, var(--hill) 36%, #6d9b3c 46%, var(--lagoon) 56%, var(--sea) 70%, #1c4466 82%);
  }
  .photo-fade {
    position: absolute; left: 0; right: 0; bottom: 0; height: 260px;
    background: linear-gradient(180deg, rgba(59,59,60,0) 0%, rgba(59,59,60,.85) 45%, var(--charcoal) 70%);
  }
  .gold-band { position: absolute; top: 0; height: 100%; width: 20px; background: var(--gold); }
  .white-rule { position: absolute; top: 0; height: 100%; width: 3px; background: var(--white); }
  .dark-panel {
    position: absolute; top: 0; height: 100%;
    background: linear-gradient(180deg, var(--charcoal) 0%, #444445 50%, var(--charcoal-deep) 100%);
  }
  .glass-bar { position: absolute; background: rgba(200,205,212,.35); }

  .brand {
    position: absolute; text-align: center; color: var(--white);
    font-family: "Cormorant Garamond", Georgia, serif; font-weight: 500;
  }
  .brand-name { font-size: 22px; letter-spacing: 4px; line-height: 1.05; text-transform: uppercase; }
  .brand-rule { width: 30px; height: 1px; background: var(--white); margin: 6px auto; }
  .brand-tag { font-size: 10px; line-height: 1.2; }

  .headline { position: absolute; left: 22px; bottom: 60px; line-height: 1.05; }
  .headline .intro { color: var(--gold-text); font-size: 25px; }
  .headline .lead { color: var(--white); font-size: 25px; }
  .headline .country { color: var(--gold-text); font-size: 33px; font-weight: 700; letter-spacing: 1px; -webkit-text-stroke: .6px var(--gold-text); }
  .site-url { position: absolute; left: 22px; bottom: 28px; color: var(--white); font-size: 10px; letter-spacing: 3.4px; }

  .contact {
    position: absolute; right: 24px; bottom: 40px; text-align: right; color: var(--white);
    font-size: 10.5px; line-height: 1.4;
  }
  .contact-title { color: var(--gold-text); font-size: 11px; font-weight: 700; margin-bottom: 6px; }
  .contact-row { display: flex; justify-content: flex-end; align-items: center; gap: 8px; margin-bottom: 4px; }
  .contact-row.phone span { font-size: 15px; }
  .contact-row svg { width: 11px; height: 11px; flex: none; }
</style>
</head>
<body>
<main class="spread">
  <!-- Back cover -->
  <section class="page back-cover">
    <div class="dark-panel" style="left:0;width:132px;"></div>
    <div class="white-rule" style="left:132px;"></div>
    <div class="gold-band" style="left:138px;"></div>
    <div class="photo" style="left:158px;right:0;" role="img" aria-label="Aerial photo of green islands, sandy bays and turquoise water with sailing boats"></div>
    <div class="glass-bar" style="left:164px;top:0;width:34px;height:220px;"></div>
    <div class="glass-bar" style="left:202px;top:0;width:6px;height:150px;"></div>
    <div class="photo-fade" style="left:158px;"></div>
    <div class="brand" style="left:0;width:132px;bottom:42px;">
      <div class="brand-name">Fern<br>Tide</div>
      <div class="brand-rule"></div>
      <div class="brand-tag">Exclusive New Zealand<br>Experiences</div>
    </div>
    <div class="contact">
      <div class="contact-title">Contact Details:</div>
      <div class="contact-row"><span>PO Box 4821, Harbour Lane West<br>Auckland 1010, New Zealand</span>
        <svg viewBox="0 0 12 12"><path d="M6 1 1 5.5h1.5V11h3V8h1v3h3V5.5H11z" fill="#a88f4e"/></svg></div>
      <div class="contact-row phone"><span>+64 9 555 0142</span>
        <svg viewBox="0 0 12 12"><path d="M3 1 1.5 2.5C1.5 7 5 10.5 9.5 10.5L11 9 8.5 7.2 7.3 8.2C5.7 7.5 4.5 6.3 3.8 4.7L4.8 3.5z" fill="#a88f4e"/></svg></div>
      <div class="contact-row"><span>hello@ferntidejourneys.example</span>
        <svg viewBox="0 0 12 12"><rect x="1" y="2.5" width="10" height="7" fill="none" stroke="#a88f4e"/><path d="M1 2.5 6 6.5 11 2.5" fill="none" stroke="#a88f4e"/></svg></div>
      <div class="contact-row"><span>www.ferntidejourneys.example</span>
        <svg viewBox="0 0 12 12"><circle cx="6" cy="6" r="4.8" fill="none" stroke="#a88f4e"/><path d="M1.2 6h9.6M6 1.2c-2.4 3-2.4 6.6 0 9.6M6 1.2c2.4 3 2.4 6.6 0 9.6" fill="none" stroke="#a88f4e" stroke-width=".8"/></svg></div>
    </div>
  </section>

  <!-- Front cover -->
  <section class="page front-cover">
    <div class="photo" style="left:0;width:290px;" role="img" aria-label="Aerial photo of a forested peninsula and sheltered bay with yachts under a blue sky"></div>
    <div class="glass-bar" style="left:228px;top:300px;width:44px;height:230px;"></div>
    <div class="glass-bar" style="left:276px;top:270px;width:8px;height:260px;"></div>
    <div class="photo-fade" style="width:290px;"></div>
    <div class="gold-band" style="left:290px;"></div>
    <div class="white-rule" style="left:316px;"></div>
    <div class="dark-panel" style="left:319px;right:0;"></div>
    <div class="brand" style="left:319px;right:0;top:60px;">
      <div class="brand-name">Fern<br>Tide</div>
      <div class="brand-rule"></div>
      <div class="brand-tag">Exclusive New Zealand<br>Experiences</div>
    </div>
    <div class="headline">
      <div class="intro">Introducing you</div>
      <div class="lead">To the very best of</div>
      <div class="country">NEW ZEALAND</div>
    </div>
    <div class="site-url">www.ferntidejourneys.example</div>
  </section>
</main>
</body>
</html>
```